Set up small scale company website

We need a website set up for our educational consultancy - Brellin Learning. We like the following site and want something similar www.quorvadeplan.co.uk We can provide the copy and images but need the following:- setting up the overall theme and design - to our requirements on colours and forma- Approximately 4 pages of services offered and with an index pageEtct (yellow and green)And the following pages - as well as a home page:- A contact page linked to our email addresses and registered business address 17 Millbrook Lane, Aldwyn, Norshire, AN4 5JP- About Us page - An index of services page that links to between 4-6 pages outlining services- A News page that links to updates of latest services, events and activities - easily updated by usOn the homepage we'd like links to twitter and LinkedIn feeds and links to our other blogs and websites
Target Market(s)
Schools, local authoroties and multi-academy trusts
Logo Text
Brellin Learning
Coding
Coded - Design and coding required
Number of Pages Required
5+ page
Font styles to use
Requirements
Should not have
- No tacky pictures of mortar boards or chalk boards etc.

```html
<!DOCTYPE html>
<html lang="en">
<head>
<meta charset="utf-8">
<title>Brellin Learning</title>
<link rel="stylesheet" href="https://fonts.googleapis.com/css2?family=Montserrat:wght@400;500;600;700&family=Open+Sans:wght@400;600&display=swap">
<style>
:root{
  --green:#7aad1f;
  --green-dark:#6a9a17;
  --yellow:#f7e21e;
  --ink:#2b2b2b;
  --muted:#555;
  --light:#f4f4f4;
  --navy:#131a2b;
  --blue-a:#2aa3e3;
  --blue-b:#1e64b0;
  --white:#fff;
}
*{box-sizing:border-box;margin:0;padding:0}
html,body{width:1200px;height:3025px;overflow:hidden}
body{font-family:"Open Sans",Arial,sans-serif;color:var(--ink);background:var(--white);position:relative}
.abs{position:absolute}
h1,h2,h3,.nav,.btn,.brand{font-family:"Montserrat",Arial,sans-serif}
.btn{position:absolute;display:flex;align-items:center;justify-content:center;border-radius:23px;font-size:13px;font-weight:600;text-transform:uppercase;color:var(--ink);text-decoration:none}
.btn-yellow{background:var(--yellow)}
.btn-green{background:var(--green);color:var(--white)}

/* header */
.site-header{position:absolute;top:0;left:0;width:1200px;height:95px;background:var(--white);z-index:5}
.brand{position:absolute;left:145px;top:26px;display:flex;align-items:center;gap:12px;font-size:31px;font-weight:700;color:#111}
.brand-dot{width:42px;height:42px;border-radius:50%;background:var(--green)}
.nav{position:absolute;top:38px;font-size:15px;color:#555;text-transform:uppercase}
.nav.active{color:var(--green)}

/* hero */
.hero{position:absolute;top:95px;left:0;width:1200px;height:630px;overflow:hidden}
.hero-photo{position:absolute;inset:0;background:linear-gradient(160deg,#8c8e92 0%,#5b6a80 40%,#3f5a86 70%,#6b7789 100%)}
.hero-shape{position:absolute;left:0;top:0}
.hero-title{position:absolute;top:372px;width:1200px;text-align:center;color:var(--white);font-size:41px;font-weight:600}
.hero-sub{position:absolute;top:424px;width:1200px;text-align:center;color:var(--white);font-size:22px;font-family:"Montserrat",sans-serif}
.hero-arrow{position:absolute;top:243px;width:38px;height:38px;border-radius:50%;background:var(--yellow)}

/* welcome */
.welcome h2{position:absolute;left:145px;top:788px;font-size:33px;font-weight:600;color:var(--green)}
.welcome p{position:absolute;left:145px;width:605px;font-size:13px;line-height:23px;color:var(--muted)}
.welcome-photo{position:absolute;left:813px;top:789px;width:242px;height:242px;border-radius:50%;border:6px solid var(--green);background:radial-gradient(circle at 50% 40%,#cfd6df,#7f8fa2)}

/* services */
.services{position:absolute;left:0;top:1085px;width:1200px;height:570px}
.services h2{position:absolute;top:92px;width:1200px;text-align:center;color:var(--white);font-size:32px;font-weight:600}
.service{position:absolute;top:164px;width:230px;text-align:center;color:var(--white)}
.service-icon{width:160px;height:160px;border-radius:50%;background:var(--white);margin:0 auto;display:flex;align-items:center;justify-content:center}
.service h3{font-size:19.5px;font-weight:500;line-height:24px;margin-top:16px;height:48px;display:flex;align-items:center;justify-content:center}
.service p{font-size:11px;line-height:15px;margin:12px auto 0;width:200px}
.service .btn{left:54px;top:300px;width:122px;height:42px}

/* latest */
.latest h2{position:absolute;top:1730px;width:1200px;text-align:center;color:var(--green);font-size:32px;font-weight:600}
.post{position:absolute;top:1805px;width:289px}
.post-photo{height:192px}
.post time{display:block;margin-top:16px;font-size:14px}
.post h3{font-family:"Open Sans",sans-serif;font-size:15px;letter-spacing:-.2px;font-weight:400;line-height:22px;margin-top:10px;white-space:nowrap}
.post p{font-size:10.5px;line-height:15px;color:var(--muted);margin-top:8px}
.chev{position:absolute;top:1885px}

/* social feed */
.feed{position:absolute;left:0;top:2285px;width:1200px;height:453px}
.tweet{position:absolute;top:125px;width:202px;height:254px;background:var(--white);box-shadow:0 1px 6px rgba(0,0,0,.15);padding:16px 16px 0}
.tweet p{font-size:13px;line-height:24.5px;color:#444}
.tweet .tag{color:var(--blue-a)}
.tweet .url{color:var(--blue-a);font-size:12.5px}
.tweet .url.alt{color:var(--green)}
.tweet-foot{position:absolute;left:16px;right:16px;top:186px;border-top:1px solid #ddd;padding-top:18px;display:flex;gap:10px}
.tweet-badge{width:30px;height:30px;border-radius:50%;flex:none}
.tweet-foot b{display:block;font-weight:400;font-size:14px;color:#444}
.tweet-foot small{font-size:10px;color:#666}

/* footer */
.site-footer{position:absolute;left:0;top:2737px;width:1200px;height:288px;background:var(--navy);color:#cfd3dc}
.site-footer h4{position:absolute;top:42px;font-family:"Montserrat",sans-serif;font-size:16px;font-weight:600;color:var(--yellow)}
.f-link{position:absolute;font-size:10.5px;color:#cfd3dc}
.f-contact{position:absolute;left:376px;font-size:10.5px;line-height:14px;display:flex;gap:14px}
.newsletter{position:absolute;left:655px;top:84px;width:218px;height:40px;background:var(--white);display:flex;align-items:center;justify-content:space-between;padding:0 12px 0 16px;font-size:11px;color:#333}
.follow{position:absolute;top:84px;width:39px;height:39px;border-radius:50%;border:1.5px solid #cfd3dc}
.f-rule{position:absolute;left:143px;top:212px;width:912px;height:1px;background:#3a4256}
.copy{position:absolute;top:244px;width:1200px;text-align:center;font-size:11px}
</style>
</head>
<body>

<header class="site-header">
  <div class="brand"><span class="brand-dot"></span>Brellin Learning</div>
  <a class="nav active" style="left:577px">Home</a>
  <a class="nav" style="left:660px">Services</a>
  <a class="nav" style="left:768px">News</a>
  <a class="nav" style="left:851px">About Us</a>
  <a class="nav" style="left:963px">Contact Us</a>
</header>

<section class="hero">
  <div class="hero-photo" role="img" aria-label="Students studying and writing at desks in a library"></div>
  <span class="hero-arrow" style="left:50px"></span>
  <span class="hero-arrow" style="left:1110px"></span>
  <svg class="abs" style="left:50px;top:243px" width="38" height="38"><path d="M22 12 L15 19 L22 26" stroke="#333" stroke-width="3" fill="none"/></svg>
  <svg class="abs" style="left:1110px;top:243px" width="38" height="38"><path d="M16 12 L23 19 L16 26" stroke="#333" stroke-width="3" fill="none"/></svg>
  <h1 class="hero-title">Brellin Learning</h1>
  <p class="hero-sub">Supporting effective learning and operations in schools, academies and trusts.</p>
  <a class="btn btn-yellow" style="left:527px;top:467px;width:146px;height:44px">Contact Us</a>
  <svg class="hero-shape" width="1200" height="630" viewBox="0 0 1200 630">
    <path d="M0 520 Q600 720 1200 520 L1200 630 L0 630 Z" fill="#fff"/>
    <path d="M0 518 Q600 718 1200 518 L1200 532 Q600 735 0 535 Z" fill="var(--green)"/>
  </svg>
</section>

<section class="welcome">
  <h2>Welcome to Brellin Learning</h2>
  <p style="top:842px">Brellin Learning Ltd offers a bespoke service to schools, Academy Trusts and Local Authorities covering all educational leadership functions from curriculum and learning to finance and operations.</p>
  <p style="top:918px">As well as consultancy we can also support change processes in school, the implementation of effective systems and interim leadership.</p>
  <a class="btn btn-green" style="left:145px;top:988px;width:148px;height:44px">Read More</a>
  <a class="btn btn-yellow" style="left:312px;top:988px;width:155px;height:44px">Contact Us</a>
  <div class="welcome-photo" role="img" aria-label="Teacher helping a student at a desk"></div>
</section>

<section class="services">
  <svg class="abs" style="left:0;top:0" width="1200" height="570"><path d="M0 80 Q600 -75 1200 80 L1200 570 L0 570 Z" fill="var(--green)"/></svg>
  <h2>Our Services</h2>
  <div class="service" style="left:133px">
    <div class="service-icon"><svg width="70" height="70" viewBox="0 0 70 70" fill="none" stroke="var(--green)" stroke-width="2"><rect x="14" y="10" width="36" height="48" transform="rotate(-8 32 34)"/><rect x="20" y="12" width="36" height="48"/><circle cx="36" cy="32" r="9"/><path d="M36 23 V32 H45"/><path d="M26 48 H50 M26 53 H44"/></svg></div>
    <h3>Centralising Finance and Operations</h3>
    <p>Aenean placerat, nibh vel accumsan aliquet, magna nibh accumsan nibh, ac tempus nunc ipsum ac tellus</p>
    <a class="btn btn-yellow">Read More</a>
  </div>
  <div class="service" style="left:367px">
    <div class="service-icon"><svg width="70" height="70" viewBox="0 0 70 70" fill="none" stroke="var(--green)" stroke-width="2"><path d="M10 58 H62"/><rect x="14" y="44" width="7" height="14"/><rect x="26" y="36" width="7" height="22"/><rect x="38" y="40" width="7" height="18"/><rect x="50" y="28" width="7" height="30"/><path d="M14 32 L28 20 L40 26 L56 12"/><circle cx="14" cy="32" r="2.5"/><circle cx="28" cy="20" r="2.5"/><circle cx="40" cy="26" r="2.5"/><circle cx="56" cy="12" r="2.5"/></svg></div>
    <h3>Curriculum Design and Budgeting</h3>
    <p>Aenean placerat, nibh vel accumsan aliquet, magna nibh accumsan nibh, ac tempus nunc ipsum ac tellus</p>
    <a class="btn btn-yellow">Read More</a>
  </div>
  <div class="service" style="left:601px">
    <div class="service-icon"><svg width="70" height="70" viewBox="0 0 70 70" fill="none" stroke="var(--green)" stroke-width="2"><rect x="26" y="10" width="32" height="46"/><circle cx="42" cy="30" r="8"/><rect x="12" y="34" width="26" height="22"/><path d="M12 40 H38 M12 46 H38"/><path d="M30 60 H56"/></svg></div>
    <h3>Finance Support</h3>
    <p>Aenean placerat, nibh vel accumsan aliquet, magna nibh accumsan nibh, ac tempus nunc ipsum ac tellus</p>
    <a class="btn btn-yellow">Read More</a>
  </div>
  <div class="service" style="left:835px">
    <div class="service-icon"><svg width="70" height="70" viewBox="0 0 70 70" fill="none" stroke="var(--green)" stroke-width="2"><circle cx="35" cy="26" r="8"/><path d="M22 56 V48 Q35 36 48 48 V56"/><circle cx="17" cy="32" r="6"/><path d="M6 56 V50 Q14 42 22 46"/><circle cx="53" cy="32" r="6"/><path d="M64 56 V50 Q56 42 48 46"/><path d="M4 58 H66"/></svg></div>
    <h3>Interim Leadership</h3>
    <p>Aenean placerat, nibh vel accumsan aliquet, magna nibh accumsan nibh, ac tempus nunc ipsum ac tellus</p>
    <a class="btn btn-yellow">Read More</a>
  </div>
</section>

<section class="latest">
  <h2>Latest Services</h2>
  <svg class="chev" style="left:44px" width="20" height="30"><path d="M15 4 L5 15 L15 26" stroke="#555" stroke-width="3" fill="none"/></svg>
  <svg class="chev" style="left:1134px" width="20" height="30"><path d="M5 4 L15 15 L5 26" stroke="#555" stroke-width="3" fill="none"/></svg>
  <article class="post" style="left:143px">
    <div class="post-photo" role="img" aria-label="Colleagues meeting around a table with papers" style="background:linear-gradient(135deg,#d9dde3,#8a97a8 60%,#3c4d6a)"></div>
    <time>4 February, 2019</time>
    <h3>Quisque aliquet ex nec est vestibulum<br>pulvinar. Pellentesque convallis.</h3>
    <p>Nunc sit amet consequat risus. Curabitur ac elit leo. In eleifend dui tellus, in scelerisque elit porttitor et. Integer eu massa lacinia, lacinia nulla non, volutpat purus.</p>
  </article>
  <article class="post" style="left:456px">
    <div class="post-photo" role="img" aria-label="Two people talking in an office" style="background:linear-gradient(135deg,#2c2f36,#6f7c8f 55%,#c7b79a)"></div>
    <time>4 February, 2019</time>
    <h3>Etiam id imperdiet lectus. Vivamus<br>lacus justo, ultrices nec.</h3>
    <p>Nunc sit amet consequat risus. Curabitur ac elit leo. In eleifend dui tellus, in scelerisque elit porttitor et. Integer eu massa lacinia, lacinia nulla non, volutpat purus.</p>
  </article>
  <article class="post" style="left:768px">
    <div class="post-photo" role="img" aria-label="Student reading in a library" style="background:linear-gradient(135deg,#4d3a2c,#8a6a4c 50%,#c9b8a2)"></div>
    <time>4 February, 2019</time>
    <h3>Fusce vitae lectus sit amet mi pulvinar<br>maximus. Aenean placerat.</h3>
    <p>Nunc sit amet consequat risus. Curabitur ac elit leo. In eleifend dui tellus, in scelerisque elit porttitor et. Integer eu massa lacinia, lacinia nulla non, volutpat purus.</p>
  </article>
  <a class="btn btn-green" style="left:527px;top:2166px;width:146px;height:44px">Read More</a>
</section>

<section class="feed">
  <svg class="abs" style="left:0;top:0" width="1200" height="453"><path d="M0 85 Q600 -5 1200 85 L1200 453 L0 453 Z" fill="var(--light)"/></svg>
  <div class="tweet" style="left:143px">
    <p>Lorem ipsum dolor it amet,<br>consectetur adipiscing its<br>sed do <span class="tag">@brellin-learning</span><br>tempor incididunt ut<br>labore et dolore magna<br><span class="url">https://brellinnotes.co.uk</span></p>
    <div class="tweet-foot"><span class="tweet-badge" style="background:var(--blue-a)"></span><div><b>@brellinlearning.</b><small>5 hour ago</small></div></div>
  </div>
  <div class="tweet" style="left:381px">
    <p>Lorem ipsum dolor it amet,<br>consectetur adipiscing its<br>sed do <span class="tag">@brellin-learning</span><br>tempor incididunt ut<br>labore et dolore magna<br><span class="url">https://brellinnotes.co.uk</span></p>
    <div class="tweet-foot"><span class="tweet-badge" style="background:var(--blue-b)"></span><div><b>@brellinlearning.</b><small>5 hour ago</small></div></div>
  </div>
  <div class="tweet" style="left:617px">
    <p>Lorem ipsum dolor it amet,<br>consectetur adipiscing its<br>sed do <span class="tag">@brellin-learning</span><br>tempor incididunt ut<br>labore et dolore magna<br><span class="url alt">https://brellinnotes.co.uk</span></p>
    <div class="tweet-foot"><span class="tweet-badge" style="background:var(--blue-a)"></span><div><b>@brellinlearning.</b><small>5 hour ago</small></div></div>
  </div>
  <div class="tweet" style="left:855px">
    <p>Lorem ipsum dolor it amet,<br>consectetur adipiscing its<br>sed do <span class="tag">@brellin-learning</span><br>tempor incididunt ut<br>labore et dolore magna<br><span class="url">https://brellinnotes.co.uk</span></p>
    <div class="tweet-foot"><span class="tweet-badge" style="background:var(--blue-b)"></span><div><b>@brellinlearning.</b><small>5 hour ago</small></div></div>
  </div>
</section>

<footer class="site-footer">
  <h4 style="left:143px">Links</h4>
  <span class="f-link" style="left:143px;top:88px">Home</span>
  <span class="f-link" style="left:143px;top:112px">Services</span>
  <span class="f-link" style="left:143px;top:136px">News</span>
  <span class="f-link" style="left:143px;top:160px">About us</span>
  <span class="f-link" style="left:216px;top:88px">Contact us</span>
  <span class="f-link" style="left:216px;top:112px">Terms and Condition</span>
  <span class="f-link" style="left:216px;top:136px">Privacy Policy</span>

  <h4 style="left:376px">Contact info</h4>
  <div class="f-contact" style="top:86px"><svg width="8" height="11" viewBox="0 0 8 11"><path d="M4 0 A4 4 0 0 1 8 4 C8 7 4 11 4 11 C4 11 0 7 0 4 A4 4 0 0 1 4 0 Z" fill="#cfd3dc"/><circle cx="4" cy="4" r="1.5" fill="var(--navy)"/></svg><span>Mr. Alan Dewsbury,<br>17 Millbrook Lane, Aldwyn, Norshire, AN4 5JP</span></div>
  <div class="f-contact" style="top:130px"><svg width="9" height="9" viewBox="0 0 10 10"><path d="M1 1 L3.5 0.5 L4.5 3 L3 4 Q4 6 6 7 L7 5.5 L9.5 6.5 L9 9 Q4 9 1 1 Z" fill="#cfd3dc"/></svg><span>Phone : 0125 480 7715</span></div>
  <div class="f-contact" style="top:154px"><svg width="10" height="8" viewBox="0 0 10 8"><rect width="10" height="8" fill="#cfd3dc"/><path d="M0 0 L5 4 L10 0" stroke="var(--navy)" fill="none"/></svg><span>Email : info@brellinlearning.co.uk</span></div>

  <h4 style="left:653px">Newsletter</h4>
  <div class="newsletter"><span>Email Address</span><svg width="20" height="14" viewBox="0 0 20 14"><rect width="20" height="14" fill="#333"/><path d="M0 0 L10 8 L20 0" stroke="#fff" stroke-width="1.5" fill="none"/></svg></div>

  <h4 style="left:918px">Follow us on</h4>
  <span class="follow" style="left:921px"></span>
  <span class="follow" style="left:967px"></span>
  <span class="follow" style="left:1016px"></span>

  <div class="f-rule"></div>
  <p class="copy">Copyright © 2019 Brellin Learning. All rights reserved.</p>
</footer>

</body>
</html>
```